Pellory T's Menu boxes

HI

This project if for the design of some illuminated menu boxes for inside a shop.

We sell Ice Cream, Milk shakes, Smoothies and some cakes.

The shop is mainly pink in colour, i have had some posters done for the windows and would like the menus to maintain the feel of the posters. i have 8 menu boards but will probably onlu use 4.

i will attach a few of the posters so you can see the feel im looking for and the menu should have:
a section for ice creams
a section for milk shakes
a section for smoothies
a section for coffees and teas
and a section for juices
and a section for desserts.

Regards
Updates

Hi

I have now attached the logos source file

Many thanks

Reason: Hi for some reason only one designer has responded therefore i am extending the deadline thanks

Hi All

I have now increased the budget on the project

Many Thanks

```html
<!DOCTYPE html>
<html lang="en">
<head>
<meta charset="utf-8">
<title>Pellory T's Ice Cream Menu</title>
<link rel="stylesheet" href="https://fonts.googleapis.com/css2?family=Boogaloo&display=swap">
<style>
  :root {
    --frame: #8c1b84;
    --panel: #ffffff;
    --band: #de1a8c;
    --ink: #111111;
    --brand: #d41785;
    --scoop-light: #f6dfe4;
    --scoop-mid: #e9b3bf;
    --scoop-deep: #c9717f;
  }
  html, body {
    margin: 0;
    padding: 0;
    width: 849px;
    height: 1200px;
    overflow: hidden;
    background: var(--frame);
  }
  .menu-board {
    position: relative;
    width: 849px;
    height: 1200px;
    background: var(--frame);
    font-family: "Boogaloo", "Arial Narrow", sans-serif;
  }
  .menu-panel {
    position: absolute;
    left: 40px;
    top: 28px;
    width: 769px;
    height: 1140px;
    background: var(--panel);
    border-radius: 22px;
    overflow: hidden;
  }
  .hero-scoop {
    position: absolute;
    right: 0;
    top: 0;
    width: 330px;
    height: 255px;
    background: radial-gradient(ellipse at 45% 65%, var(--scoop-light) 0%, var(--scoop-mid) 55%, var(--scoop-deep) 100%);
    border-bottom-left-radius: 120px;
  }
  .brand-name {
    position: absolute;
    left: 28px;
    top: 62px;
    margin: 0;
    font-size: 64px;
    font-weight: 400;
    color: var(--brand);
    line-height: 1;
  }
  .band {
    position: absolute;
    left: 5px;
    width: 759px;
    height: 46px;
    background: var(--band);
  }
  .menu-item {
    position: absolute;
    left: 50px;
    width: 690px;
    display: flex;
    justify-content: space-between;
    align-items: center;
    height: 60px;
    font-size: 40px;
    color: var(--ink);
  }
</style>
</head>
<body>
  <main class="menu-board">
    <section class="menu-panel">
      <div class="hero-scoop" role="img" aria-label="Photo of scoops of strawberry and chocolate chip ice cream"></div>
      <h1 class="brand-name">Pellory T's</h1>

      <div class="band" style="top:255px"></div>
      <div class="menu-item" style="top:332px"><span>Chocolate Chip</span><span>5$</span></div>

      <div class="band" style="top:416px"></div>
      <div class="menu-item" style="top:494px"><span>Mint Chocolate Chip</span><span>5$</span></div>

      <div class="band" style="top:575px"></div>
      <div class="menu-item" style="top:650px"><span>Caramel Pecan Swirl</span><span>5$</span></div>

      <div class="band" style="top:736px"></div>
      <div class="menu-item" style="top:811px"><span>Sunny Summer Strawberry</span><span>5$</span></div>

      <div class="band" style="top:892px"></div>
      <div class="menu-item" style="top:978px"><span>Chocolate Chip Cookie Dough</span><span>5$</span></div>

      <div class="band" style="top:1059px"></div>
    </section>
  </main>
</body>
</html>
```